Website for QuillarionCrew presentation

We need a new website, ideally as a wordpress there, for QuillarionCrew - we focus on machine learning, big data, data science and data analytics. This website should have two main sections - team presentation, introduction and offered services as static pages, and a blog section.

Target Market(s)

Companies which would like to hire the consultants for data science

Industry/Entity Type

Data Service

Font styles to use
Sans Serif

Colors

Designer to choose colors to be used in the design.

Requirements
Must have
• Wordpress template, blog and presentation pages, nice background images, incorporate the existing logo from brief
Nice to have
• match the word and ppt existing templates for quillarion crew

```html
<!DOCTYPE html>
<html lang="en">
<head>
<meta charset="utf-8">
<title>QuillarionCrew — Data Science Consultants</title>
<link rel="stylesheet" href="https://fonts.googleapis.com/css2?family=Montserrat:wght@400;500;600;700&family=Arimo:wght@400;700&display=swap">
<style>
  :root {
    --brand: #1b7dc0;
    --brand-dark: #16679f;
    --ink: #222;
    --body: #555;
    --muted: #777;
    --line: #dcdfe3;
    --footer: #1f1f1f;
    --footer-line: #3a3a3a;
    --white: #fff;
    --heading: "Montserrat", sans-serif;
    --text: "Arimo", sans-serif;
  }
  * { box-sizing: border-box; margin: 0; padding: 0; }
  html, body { width: 1200px; height: 2507px; overflow: hidden; }
  body { position: relative; background: var(--white); font-family: var(--text); color: var(--body); }
  .abs { position: absolute; }

  /* header */
  .site-header { position: absolute; left: 0; top: 0; width: 1200px; height: 105px; border-top: 4px solid var(--brand); background: var(--white); }
  .brand { position: absolute; left: 87px; top: 26px; display: flex; align-items: center; gap: 12px; font-family: var(--heading); font-weight: 700; font-size: 22px; line-height: 24px; color: var(--brand); letter-spacing: .5px; }
  .brand-name { display: block; }
  .brand-dot { flex: none; width: 30px; height: 30px; border-radius: 50%; background: var(--brand); }
  .main-nav { position: absolute; top: 49px; font-family: var(--heading); font-weight: 500; font-size: 12.5px; color: var(--ink); }
  .main-nav span { position: absolute; white-space: nowrap; }
  .main-nav .active { color: var(--brand); }
  .search-btn { position: absolute; left: 1061px; top: 31px; width: 50px; height: 50px; border: 2px solid var(--brand); border-radius: 50%; display: flex; align-items: center; justify-content: center; }

  /* hero */
  .hero { position: absolute; left: 0; top: 105px; width: 1200px; height: 513px;
    background: radial-gradient(ellipse at 72% 35%, #4a7fd6 0%, #27508f 30%, #1b3564 60%, #132645 100%); }

  /* welcome */
  .section-title { font-family: var(--heading); font-weight: 500; font-size: 23px; color: var(--brand); letter-spacing: .3px; }
  .rule { position: absolute; height: 3px; width: 87px; background: var(--brand); }
  .welcome-copy { position: absolute; left: 87px; width: 530px; font-size: 11.5px; line-height: 26.7px; color: var(--body); }
  .btn { position: absolute; left: 87px; top: 977px; width: 129px; height: 41px; background: var(--brand); border-radius: 3px; color: var(--white); font-family: var(--heading); font-weight: 500; font-size: 12.5px; display: flex; align-items: center; justify-content: center; }
  .welcome-visual { position: absolute; left: 677px; top: 682px; width: 436px; height: 309px; border: 4px solid #5e5e5e;
    background: radial-gradient(ellipse at 40% 45%, #2d6cf0 0%, #1336b0 40%, #07124d 80%); }

  /* team */
  .team { position: absolute; left: 0; top: 1073px; width: 1200px; height: 601px;
    background: linear-gradient(120deg, #eef3f9 0%, #f8fafc 45%, #eef1f6 100%); }
  .centered { position: absolute; left: 0; width: 1200px; text-align: center; }
  .lede { font-size: 11.5px; color: var(--body); }
  .member-card { position: absolute; width: 498px; height: 162px; background: rgba(255,255,255,.94); border: 2px solid #e1e5ea; box-shadow: 0 2px 6px rgba(0,0,0,.06); }
  .member-photo { position: absolute; left: 27px; top: 21px; width: 120px; height: 120px; border-radius: 50%; border: 2px solid var(--brand); padding: 4px; }
  .member-photo div { width: 100%; height: 100%; border-radius: 50%; background: linear-gradient(160deg, #c9b8a6, #7a6658); }
  .member-name { position: absolute; left: 174px; top: 20px; font-family: var(--heading); font-weight: 600; font-size: 14px; color: var(--brand); }
  .member-date { position: absolute; left: 174px; top: 42px; font-size: 12px; color: var(--muted); }
  .member-bio { position: absolute; left: 174px; top: 72px; width: 300px; font-size: 11px; line-height: 23px; color: var(--body); }

  /* blog */
  .feature-image { position: absolute; left: 87px; top: 1841px; width: 521px; height: 328px;
    background: radial-gradient(ellipse at 50% 40%, #2f6fd0 0%, #17429a 45%, #0b2361 100%); }
  .feature-card { position: absolute; left: 150px; top: 2055px; width: 480px; height: 134px; background: var(--white); border: 1px solid var(--line); }
  .post-title { font-family: var(--heading); font-weight: 500; font-size: 13px; color: var(--ink); }
  .post-date { font-family: var(--heading); font-weight: 600; font-size: 11.5px; color: var(--brand); display: flex; align-items: center; gap: 6px; }
  .post-text { font-size: 11px; line-height: 23px; color: var(--body); }
  .read-more { font-family: var(--heading); font-weight: 600; font-size: 10.5px; color: var(--brand); text-decoration: underline; }
  .thumb { position: absolute; left: 655px; width: 164px; height: 144px; }
  .thumb-tech { top: 1841px; background: radial-gradient(ellipse at 55% 50%, #3d5d6a 0%, #18262e 70%); }
  .thumb-desk { top: 2033px; background: linear-gradient(135deg, #e9e4dc 0%, #b7ada0 60%, #7d7268 100%); }
  .post-side { position: absolute; left: 847px; width: 240px; }

  /* footer */
  .site-footer { position: absolute; left: 0; top: 2257px; width: 1200px; height: 250px; background: var(--footer); color: var(--white); }
  .footer-brand { position: absolute; left: 170px; top: 52px; width: 280px; display: flex; align-items: center; gap: 14px; font-family: var(--heading); font-weight: 700; font-size: 28px; line-height: 32px; color: var(--brand); letter-spacing: .5px; }
  .footer-brand .brand-dot { width: 36px; height: 36px; }
  .footer-heading { position: absolute; top: 32px; font-family: var(--heading); font-weight: 500; font-size: 15px; color: var(--white); }
  .footer-link { position: absolute; font-size: 12px; color: var(--white); white-space: nowrap; }
  .newsletter-input { position: absolute; left: 764px; top: 109px; width: 292px; height: 43px; background: var(--white); font-size: 11.5px; color: #666; padding-left: 18px; display: flex; align-items: center; }
  .newsletter-send { position: absolute; left: 1056px; top: 109px; width: 45px; height: 43px; background: var(--brand); display: flex; align-items: center; justify-content: center; }
  .footer-rule { position: absolute; left: 87px; top: 181px; width: 1026px; height: 1px; background: var(--footer-line); }
  .copyright { position: absolute; left: 0; top: 208px; width: 1200px; text-align: center; font-size: 11.5px; color: var(--white); }
</style>
</head>
<body>

<header class="site-header">
  <div class="brand"><span class="brand-dot"></span><span><span class="brand-name">QUILLARION</span><span class="brand-name">CREW</span></span></div>
  <nav class="main-nav">
    <span class="active" style="left:498px">HOME</span>
    <span style="left:585px">ABOUT US</span>
    <span style="left:697px">SERVICES</span>
    <span style="left:807px">TEAM</span>
    <span style="left:891px">BLOG</span>
    <span style="left:974px">CONTACT US</span>
  </nav>
  <div class="search-btn">
    <svg width="14" height="14" viewBox="0 0 14 14"><circle cx="6" cy="6" r="4.2" fill="none" stroke="#1b7dc0" stroke-width="2"/><line x1="9" y1="9" x2="12.5" y2="12.5" stroke="#1b7dc0" stroke-width="2"/></svg>
  </div>
</header>

<section class="hero" role="img" aria-label="Hand touching a hexagon grid of data science terms: machine learning, artificial intelligence, algorithms, statistics, prediction"></section>

<section class="welcome">
  <h1 class="section-title abs" style="left:87px;top:672px">WELCOME TO QUILLARION CREW</h1>
  <div class="rule" style="left:87px;top:716px"></div>
  <p class="welcome-copy" style="top:744px">Sed ut perspiciatis unde omnis iste natus error sit voluptatem accusantium doloremque laudantium, totam rem aperiam, eaque ipsa quae ab illo inventore veritatis et quasi architecto beatae vitae dicta sunt explicabo. Nemo enim ipsam voluptatem quia voluptas sit aspernatur aut odit aut fugit, sed quia consequuntur magni dolores eos qui ratione voluptatem sequi nesciunt.</p>
  <p class="welcome-copy" style="top:871px">Neque porro quisquam est, qui dolorem ipsum quia dolor sit amet, consectetur, adipisci velit, sed quia non numquam eius modi tempora incidunt ut labore et dolore magnam aliquam quaerat voluptatem. Ut enim ad minima veniam, quis nostrum exercitationem ullam corporis</p>
  <div class="btn">READ MORE</div>
  <div class="welcome-visual" role="img" aria-label="Glowing blue circuit board shaped like a brain with binary digits"></div>
</section>

<section class="team">
  <h2 class="section-title centered" style="top:42px;font-size:26px">OUR TEAM</h2>
  <div class="rule" style="left:565px;top:86px;width:70px"></div>
  <p class="centered lede" style="top:108px">Sed ut perspiciatis unde omnis iste natus error sit voluptatem accusantium doloremque laudantium</p>

  <article class="member-card" style="left:87px;top:172px">
    <div class="member-photo"><div role="img" aria-label="Portrait of team member"></div></div>
    <h3 class="member-name">JHON SMITH</h3>
    <p class="member-date">Posed on 03 July 2018</p>
    <p class="member-bio">Sed ut perspiciatis unde omnis iste natus error sit voluptatem accusantium doloremque laudantium, totam rem beatae vitae dicta sunt explicabo.</p>
  </article>
  <article class="member-card" style="left:613px;top:172px">
    <div class="member-photo"><div role="img" aria-label="Portrait of team member"></div></div>
    <h3 class="member-name">JHON SMITH</h3>
    <p class="member-date">Posed on 03 July 2018</p>
    <p class="member-bio">Sed ut perspiciatis unde omnis iste natus error sit voluptatem accusantium doloremque laudantium, totam rem beatae vitae dicta sunt explicabo.</p>
  </article>
  <article class="member-card" style="left:87px;top:367px">
    <div class="member-photo"><div role="img" aria-label="Portrait of team member"></div></div>
    <h3 class="member-name">JHON SMITH</h3>
    <p class="member-date">Posed on 03 July 2018</p>
    <p class="member-bio">Sed ut perspiciatis unde omnis iste natus error sit voluptatem accusantium doloremque laudantium, totam rem beatae vitae dicta sunt explicabo.</p>
  </article>
  <article class="member-card" style="left:613px;top:367px">
    <div class="member-photo"><div role="img" aria-label="Portrait of team member"></div></div>
    <h3 class="member-name">JHON SMITH</h3>
    <p class="member-date">Posed on 03 July 2018</p>
    <p class="member-bio">Sed ut perspiciatis unde omnis iste natus error sit voluptatem accusantium doloremque laudantium, totam rem beatae vitae dicta sunt explicabo.</p>
  </article>
</section>

<section class="blog">
  <h2 class="section-title centered" style="top:1715px;font-size:26px">LATEST BLOG</h2>
  <div class="rule" style="left:565px;top:1760px;width:70px"></div>
  <p class="centered lede" style="top:1782px">Sed ut perspiciatis unde omnis iste natus error sit voluptatem accusantium doloremque laudantium</p>

  <div class="feature-image" role="img" aria-label="Businessman with glowing machine learning and AI technology icons"></div>
  <article class="feature-card">
    <h3 class="post-title abs" style="left:22px;top:22px">SED UT PERSPICIATIS UNDE OMNIS ISTE</h3>
    <span class="post-date abs" style="left:373px;top:22px">
      <svg width="11" height="11" viewBox="0 0 11 11"><rect x="1" y="2" width="9" height="8" fill="none" stroke="#1b7dc0" stroke-width="1.4"/><line x1="1" y1="4.5" x2="10" y2="4.5" stroke="#1b7dc0" stroke-width="1.4"/><line x1="3.5" y1="0.5" x2="3.5" y2="3" stroke="#1b7dc0" stroke-width="1.4"/><line x1="7.5" y1="0.5" x2="7.5" y2="3" stroke="#1b7dc0" stroke-width="1.4"/></svg>JUNE 21,2018</span>
    <p class="post-text abs" style="left:22px;top:50px;width:440px">Sed ut perspiciatis unde omnis iste natus error sit voluptatem accusantium dolo itatis et quasi architecto beatae vitae dicta sunt explicabo.</p>
    <a class="read-more abs" style="left:22px;top:104px">READ MORE</a>
  </article>

  <div class="thumb thumb-tech" role="img" aria-label="Hands holding a glowing holographic network"></div>
  <article class="post-side" style="top:1843px">
    <h3 class="post-title">SED UT PERSPICIATIS</h3>
    <span class="post-date" style="margin-top:10px">
      <svg width="11" height="11" viewBox="0 0 11 11"><rect x="1" y="2" width="9" height="8" fill="none" stroke="#1b7dc0" stroke-width="1.4"/><line x1="1" y1="4.5" x2="10" y2="4.5" stroke="#1b7dc0" stroke-width="1.4"/></svg>JUNE 21,2018</span>
    <p class="post-text" style="margin-top:4px;width:225px">Sed ut perspiciatis unde omnis iste natus error sit voluptatem accusantium dolore mque laudantium, totam</p>
    <a class="read-more" style="display:block;margin-top:4px">READ MORE</a>
  </article>

  <div class="thumb thumb-desk" role="img" aria-label="Desk with printed analytics charts and a laptop"></div>
  <article class="post-side" style="top:2035px">
    <h3 class="post-title">SED UT PERSPICIATIS</h3>
    <span class="post-date" style="margin-top:10px">
      <svg width="11" height="11" viewBox="0 0 11 11"><rect x="1" y="2" width="9" height="8" fill="none" stroke="#1b7dc0" stroke-width="1.4"/><line x1="1" y1="4.5" x2="10" y2="4.5" stroke="#1b7dc0" stroke-width="1.4"/></svg>JUNE 21,2018</span>
    <p class="post-text" style="margin-top:4px;width:225px">Sed ut perspiciatis unde omnis iste natus error sit voluptatem accusantium dolore mque laudantium, totam</p>
    <a class="read-more" style="display:block;margin-top:4px">READ MORE</a>
  </article>
</section>

<footer class="site-footer">
  <div class="footer-brand"><span class="brand-dot"></span><span><span class="brand-name">QUILLARION</span><span class="brand-name">CREW</span></span></div>

  <h4 class="footer-heading" style="left:496px">QUICK LINKS</h4>
  <span class="footer-link" style="left:498px;top:73px">Home</span>
  <span class="footer-link" style="left:498px;top:103px">About Us</span>
  <span class="footer-link" style="left:498px;top:132px">Services</span>
  <span class="footer-link" style="left:618px;top:73px">Team</span>
  <span class="footer-link" style="left:618px;top:103px">Blog</span>
  <span class="footer-link" style="left:618px;top:132px">Contact Us</span>

  <h4 class="footer-heading" style="left:764px">NEWSLETTER</h4>
  <span class="footer-link" style="left:764px;top:73px">Sed ut perspiciatis unde omnis iste natus error sit</span>
  <div class="newsletter-input">Enter Your Email Id :</div>
  <div class="newsletter-send">
    <svg width="16" height="16" viewBox="0 0 16 16"><path d="M1 7.5 L15 1 L10 15 L7.5 9 Z" fill="#fff"/></svg>
  </div>

  <div class="footer-rule"></div>
  <p class="copyright">© Copy Right -2018 QuillarionCrew . All rights reserved.</p>
</footer>

</body>
</html>
```